Der Designer hat mir ein super Logo entworfen sehr schnell tolle Zusammenarbeit. Ist nur zu empfehlen
Zielgruppe
Es handelt sich um eine Haus und Immobilienverwaltung die Zielgruppe sind Eigentümer der Häuser und Firmen
Aufgabenstellung
Edel klassisch

```html
<!DOCTYPE html>
<html lang="de">
<head>
<meta charset="utf-8">
<title>Velmark Verwaltungsgruppe – Visitenkarte</title>
<link href="https://fonts.googleapis.com/css2?family=Arimo:wght@400&display=swap" rel="stylesheet">
<style>
  :root {
    --stage: #4b4b4b;
    --card-dark: #363636;
    --card-light: #ffffff;
    --brand-grey: #b5b5b5;
    --brand-blue: #79b0cc;
    --brand-green: #86a996;
    --name-olive: #7d7f74;
    --text: #5a5a5a;
    --divider: #dcdcdc;
  }
  * { margin: 0; padding: 0; box-sizing: border-box; }
  html, body { width: 1200px; height: 1200px; overflow: hidden; }
  body {
    background: var(--stage);
    font-family: "Arimo", Arial, sans-serif;
    position: relative;
  }
  .card { position: absolute; width: 467px; height: 301px; }
  .card--front { left: 366px; top: 257px; background: var(--card-dark); }
  .card--back { left: 377px; top: 671px; background: var(--card-light); }

  .brand {
    position: absolute;
    display: flex;
    align-items: center;
    gap: 10px;
    color: var(--brand-grey);
    font-weight: 400;
    text-transform: uppercase;
    white-space: nowrap;
  }
  .brand__mark { background: var(--brand-blue); flex: none; }
  .brand__name { line-height: 1.25; }

  .card--front .brand { left: 0; right: 0; top: 104px; justify-content: center; }
  .card--front .brand__mark { width: 22px; height: 22px; }
  .card--front .brand__name { font-size: 21px; letter-spacing: 3px; text-align: center; }

  .card--back .brand { right: 27px; top: 52px; gap: 7px; }
  .card--back .brand__mark { width: 12px; height: 12px; }
  .card--back .brand__name { font-size: 11.5px; letter-spacing: 1.6px; text-align: right; }

  .divider {
    position: absolute; left: 193px; top: 22px;
    width: 1px; height: 226px; background: var(--divider);
  }
  .person { position: absolute; left: 0; width: 186px; top: 113px; text-align: center; }
  .person__name { font-size: 21px; color: var(--name-olive); }
  .person__role { font-size: 11px; color: #7a7a7a; margin-top: 4px; }

  .contact { position: absolute; right: 27px; top: 145px; width: 210px; color: var(--text); }
  .contact__address { font-size: 12.5px; text-align: right; white-space: nowrap; }
  .contact__heading { font-size: 13px; color: var(--brand-green); text-align: right; margin-top: 10px; }
  .contact__row { display: flex; justify-content: space-between; font-size: 12.5px; margin-top: 6px; white-space: nowrap; }
  .contact__label { color: var(--brand-blue); }

  .band { position: absolute; top: 262px; height: 12px; }
  .band--grey { left: 0; width: 90px; background: var(--brand-grey); }
  .band--green { left: 90px; right: 0; background: var(--brand-green); }
</style>
</head>
<body>
  <section class="card card--front">
    <div class="brand">
      <span class="brand__mark"></span>
      <span class="brand__name">Velmark<br>Verwaltungsgruppe GmbH</span>
    </div>
  </section>

  <section class="card card--back">
    <div class="brand">
      <span class="brand__mark"></span>
      <span class="brand__name">Velmark<br>Verwaltungsgruppe GmbH</span>
    </div>

    <div class="person">
      <p class="person__name">Lena Brandhorst</p>
      <p class="person__role">Geschäftsführer</p>
    </div>

    <div class="divider"></div>

    <div class="contact">
      <p class="contact__address">Lindenhofweg 12 | 10823 Berlin</p>
      <p class="contact__heading">Kontakt</p>
      <p class="contact__row"><span class="contact__label">Telefon:</span><span>+49 030 512 77 904</span></p>
      <p class="contact__row"><span class="contact__label">Telefax:</span><span>+49 030 512 77 904</span></p>
      <p class="contact__row"><span class="contact__label">E-Mail:</span><span>kontakt@velmark-gruppe.de</span></p>
    </div>

    <div class="band band--grey"></div>
    <div class="band band--green"></div>
  </section>
</body>
</html>
```